Real Estate Development Company Stationary

We need our company, business card, letterhead, pocket folder and envelope designed.

We are a new real estate development company. We focus on data centre, commercial and real estate development.

Please see attached for our logo. Since it's a new logo, you still can make minor adjust if you like it makes senses

The client has sent me a business card he really likes. Please see file 3.

Target Market(s)

Real Estate Investors
Large corporations
Home buyers

Industry/Entity Type

Real Estate

```html
<!DOCTYPE html>
<html lang="en">
<head>
<meta charset="utf-8">
<title>Verano Development Inc. – Stationery Set</title>
<link rel="stylesheet" href="https://fonts.googleapis.com/css2?family=Montserrat:wght@400;500;600;700&display=swap">
<style>
  :root {
    --navy: #263f73;
    --navy-soft: #2f4a82;
    --green: #7cb342;
    --paper: #f7f7f7;
    --ink: #3a3f4a;
    --muted: #8a8f99;
    --backdrop: #e9e9ea;
  }
  * { box-sizing: border-box; margin: 0; padding: 0; }
  html, body { width: 1200px; height: 882px; overflow: hidden; }
  body {
    background: var(--backdrop);
    font-family: "Montserrat", Arial, sans-serif;
    color: var(--ink);
    position: relative;
  }
  .sheet { position: absolute; box-shadow: 0 2px 6px rgba(0,0,0,.12); }
  .paper { background: var(--paper); }
  .navy { background: var(--navy); color: #fff; }

  .brand { display: flex; align-items: center; gap: 6px; }
  .brand-square { width: 10px; height: 10px; background: var(--navy); flex: none; }
  .brand-name { font-weight: 600; color: var(--green); font-size: 12px; letter-spacing: .2px; white-space: nowrap; }
  .navy .brand-square { background: var(--green); }

  /* Letterhead */
  .letterhead { left: 40px; top: 50px; width: 310px; height: 438px; padding: 30px 28px; }
  .letterhead .salutation { margin-top: 34px; font-size: 9px; font-weight: 600; }
  .letterhead .body-copy { margin-top: 10px; font-size: 7px; line-height: 1.7; color: var(--ink); }
  .letterhead .body-copy p + p { margin-top: 8px; }
  .letterhead .closing { margin-top: 14px; font-size: 7px; }
  .letterhead .signer { font-size: 8px; font-weight: 700; color: var(--navy); margin-top: 2px; }
  .signature-area { width: 80px; height: 26px; background: #e6e9f1; margin-top: 6px; }
  .letterhead .footer { position: absolute; left: 28px; right: 28px; bottom: 22px; display: flex; justify-content: space-between; font-size: 6px; color: var(--muted); line-height: 1.6; }
  .contact-line { display: flex; align-items: center; gap: 4px; }
  .contact-line i { width: 6px; height: 6px; background: var(--green); display: inline-block; }

  /* Folder */
  .folder { left: 380px; top: 50px; width: 300px; height: 438px; padding: 34px 28px; }
  .folder .brand { justify-content: center; }
  .folder .web { position: absolute; right: 24px; bottom: 20px; font-size: 6px; opacity: .8; }

  /* Envelopes */
  .envelope-front { left: 710px; top: 50px; width: 450px; height: 220px; padding: 24px 26px; }
  .envelope-front .address { position: absolute; left: 26px; bottom: 22px; font-size: 6px; color: var(--muted); line-height: 1.6; }
  .envelope-front .corner-band { position: absolute; right: 0; top: 0; width: 10px; height: 100%; background: var(--green); }
  .envelope-back { left: 710px; top: 290px; width: 450px; height: 200px; }
  .envelope-back .flap { height: 70px; background: var(--navy); border-radius: 0 0 18px 18px; display: flex; align-items: flex-end; justify-content: center; padding-bottom: 12px; }
  .envelope-back .seal { width: 10px; height: 10px; background: var(--green); }

  /* Business cards */
  .card { width: 230px; height: 130px; }
  .card-back { left: 40px; top: 520px; padding: 16px 16px; }
  .card-back .holder { text-align: right; margin-top: -10px; }
  .card-back .holder-name { font-size: 8px; font-weight: 700; color: var(--navy); }
  .card-back .holder-role { font-size: 6px; color: var(--muted); }
  .card-back .details { position: absolute; left: 16px; right: 16px; bottom: 14px; display: flex; justify-content: space-between; font-size: 5.5px; color: var(--muted); line-height: 1.7; }
  .card-front { left: 40px; top: 670px; display: flex; align-items: center; justify-content: center; }

  /* Notebook */
  .notebook { left: 320px; top: 520px; width: 250px; height: 340px; padding: 40px 26px 0 34px; }
  .notebook .binding { position: absolute; left: 8px; top: 10px; bottom: 10px; width: 10px;
    background: repeating-linear-gradient(to bottom, #b9bcc4 0 3px, transparent 3px 8px); }
  .notebook .brand { justify-content: center; }
  .notebook .web { position: absolute; right: 18px; bottom: 18px; font-size: 6px; opacity: .8; }
</style>
</head>
<body>

  <section class="sheet paper letterhead" aria-label="Letterhead">
    <div class="brand"><span class="brand-square"></span><span class="brand-name">Verano Development Inc.</span></div>
    <p class="salutation">Dear sir / madame,</p>
    <div class="body-copy">
      <p>Thank you for your interest in our upcoming projects. We are pleased to share an overview of our commercial and data centre developments for the coming year.</p>
      <p>Please find the enclosed brochure and site plans. Our team will contact you shortly to arrange a meeting.</p>
    </div>
    <p class="closing">Yours Sincerely,</p>
    <p class="signer">Dana Rowe</p>
    <div class="signature-area" role="img" aria-label="Handwritten signature"></div>
    <div class="footer">
      <div>
        <div class="contact-line"><i></i>(555) 014 2281</div>
        <div class="contact-line"><i></i>(555) 014 2282</div>
      </div>
      <div>
        <div class="contact-line"><i></i>hello@veranodev.com</div>
        <div class="contact-line"><i></i>www.veranodev.com</div>
      </div>
      <div>
        <div>Unit 4, 220 Harbour Road</div>
        <div>Eastfield, NY 10021</div>
      </div>
    </div>
  </section>

  <section class="sheet navy folder" aria-label="Pocket folder">
    <div class="brand"><span class="brand-square"></span><span class="brand-name">Verano Development Inc.</span></div>
    <p class="web">www.veranodev.com</p>
  </section>

  <section class="sheet paper envelope-front" aria-label="Envelope front">
    <div class="brand"><span class="brand-square"></span><span class="brand-name">Verano Development Inc.</span></div>
    <div class="address">
      <div>Unit 4, 220 Harbour Road</div>
      <div>Eastfield, NY 10021</div>
    </div>
    <span class="corner-band"></span>
  </section>

  <section class="sheet paper envelope-back" aria-label="Envelope back">
    <div class="flap"><span class="seal"></span></div>
  </section>

  <section class="sheet paper card card-back" aria-label="Business card back">
    <div class="brand"><span class="brand-square"></span><span class="brand-name">Verano Development Inc.</span></div>
    <div class="holder" style="margin-top:14px">
      <p class="holder-name">Jordan Pell</p>
      <p class="holder-role">Manager</p>
    </div>
    <div class="details">
      <div>
        <div class="contact-line"><i></i>(555) 014 2281</div>
        <div class="contact-line"><i></i>(555) 014 2282</div>
      </div>
      <div>
        <div>hello@veranodev.com</div>
        <div>www.veranodev.com</div>
      </div>
      <div>
        <div>Unit 4, 220 Harbour Road</div>
        <div>Eastfield, NY 10021</div>
      </div>
    </div>
  </section>

  <section class="sheet navy card card-front" aria-label="Business card front">
    <div class="brand"><span class="brand-square"></span><span class="brand-name">Verano Development Inc.</span></div>
  </section>

  <section class="sheet navy notebook" aria-label="Notebook cover">
    <span class="binding"></span>
    <div class="brand"><span class="brand-square"></span><span class="brand-name">Verano Development Inc.</span></div>
    <p class="web">www.veranodev.com</p>
  </section>

</body>
</html>
```